Modernise Business Card

Our company has been operating for 10 years. With the start of the new decade we are looking to refresh our business card design. We manufacture a range of industrial product shipping to customers internationally. A copy of our current card, both sides, is attached. We are looking for a mature professional appearance.

```html
<!DOCTYPE html>
<html lang="en">
<head>
<meta charset="utf-8">
<title>Veltrix Business Card</title>
<link href="https://fonts.googleapis.com/css2?family=Montserrat:wght@400;600;700&display=swap" rel="stylesheet">
<style>
  :root {
    --band-blue: #05ade3;
    --brand-blue: #1d9bd9;
    --ink: #1f1f1f;
    --card: #ffffff;
    --page: #ffffff;
  }
  * { margin: 0; padding: 0; box-sizing: border-box; }
  html, body { width: 1200px; height: 1200px; overflow: hidden; background: var(--page); }
  body { position: relative; font-family: "Montserrat", Arial, sans-serif; color: var(--ink); }

  .card {
    position: absolute;
    left: 181px;
    width: 840px;
    height: 480px;
    background: var(--card);
    border-radius: 38px;
    box-shadow: 0 4px 10px rgba(0,0,0,0.28);
    overflow: hidden;
  }
  .card--front { top: 78px; }
  .card--back { top: 622px; height: 478px; }

  .wordmark {
    position: absolute;
    font-weight: 700;
    color: var(--brand-blue);
    letter-spacing: -1px;
    line-height: 1;
    white-space: nowrap;
  }
  .card--front .wordmark {
    left: 0; right: 0; top: 182px;
    text-align: center;
    font-size: 108px;
  }
  .card--back .wordmark {
    right: 34px; top: 42px;
    font-size: 76px;
  }

  .tagline-band {
    position: absolute;
    left: 0; right: 0; bottom: 0;
    height: 89px;
    background: var(--band-blue);
    display: flex;
    align-items: center;
    justify-content: center;
  }
  .tagline {
    color: #fff;
    font-weight: 700;
    font-size: 22px;
    letter-spacing: 0.2px;
  }

  .name-accent {
    position: absolute;
    left: 0; top: 44px;
    width: 9px; height: 36px;
    background: var(--band-blue);
  }
  .person-name {
    position: absolute;
    left: 28px; top: 43px;
    font-size: 34px;
    font-weight: 600;
    color: var(--band-blue);
  }

  .address {
    position: absolute;
    left: 28px; top: 200px;
    font-size: 21px;
    line-height: 30px;
    font-style: normal;
  }

  .contacts {
    position: absolute;
    left: 28px; top: 330px;
    list-style: none;
    font-size: 21px;
    line-height: 30px;
  }
  .contacts li { display: flex; align-items: center; }
  .contacts svg { width: 22px; height: 22px; margin-right: 8px; flex: none; }
</style>
</head>
<body>

<section class="card card--front">
  <div class="wordmark">Veltrix</div>
  <div class="tagline-band">
    <p class="tagline">Hydraulic Adapters | Hose Fittings | Quick Couplings</p>
  </div>
</section>

<section class="card card--back">
  <span class="name-accent"></span>
  <h1 class="person-name">Sam Arden</h1>
  <div class="wordmark">Veltrix</div>

  <address class="address">
    2208-5, Lin Feng Tower<br>
    114 Qiaoyuan Road, Haishu District<br>
    Taizhou 318000 China
  </address>

  <ul class="contacts">
    <li>
      <svg viewBox="0 0 24 24" aria-hidden="true"><path fill="#1d9bd9" d="M6.6 3.5l2.6 3.2-1.7 2.1c1.2 2.6 3.2 4.6 5.8 5.8l2.1-1.7 3.2 2.6-1.5 3.3c-6.9-.4-12.4-5.9-12.8-12.8z"/><path d="M14 4a6 6 0 0 1 6 6M14 7.5a2.5 2.5 0 0 1 2.5 2.5" stroke="#1d9bd9" stroke-width="1.6" fill="none"/></svg>
      +86 139 5520 7714 (China)
    </li>
    <li>
      <svg viewBox="0 0 24 24" aria-hidden="true"><path fill="#1d9bd9" d="M6.6 3.5l2.6 3.2-1.7 2.1c1.2 2.6 3.2 4.6 5.8 5.8l2.1-1.7 3.2 2.6-1.5 3.3c-6.9-.4-12.4-5.9-12.8-12.8z"/><path d="M14 4a6 6 0 0 1 6 6M14 7.5a2.5 2.5 0 0 1 2.5 2.5" stroke="#1d9bd9" stroke-width="1.6" fill="none"/></svg>
      +61 412 880 391 (Australia)
    </li>
    <li>
      <svg viewBox="0 0 24 24" aria-hidden="true"><rect x="1" y="5" width="22" height="14" fill="#1d9bd9"/><path d="M1 5l11 8 11-8" stroke="#fff" stroke-width="1.6" fill="none"/></svg>
      sarden@veltrixfittings.com
    </li>
    <li>
      <svg viewBox="0 0 24 24" aria-hidden="true"><circle cx="12" cy="12" r="10.5" fill="#1d9bd9"/><ellipse cx="12" cy="12" rx="4.5" ry="10.5" stroke="#fff" stroke-width="1.3" fill="none"/><path d="M1.5 12h21M3.5 7h17M3.5 17h17" stroke="#fff" stroke-width="1.3"/></svg>
      www.veltrixfittings.com
    </li>
  </ul>
</section>

</body>
</html>
```